Harnwick Aerial Services, LLC - Business Card

I currently have a drone business that specializes in aerial photography, thermal image inspections, deer recovery, search and rescue, custom agricultural applications. i will attach my current business card as well as some logos to incorporate for a new up to date business card
Updates

Designs look the same

Sick

Target Market(s)

farmers, hunters

Contact Information for Business Card

name address phone number (as existing card i attached)

Requirements
Must have
• im good with existing business card, but would like an agricultural twist

```html
<!DOCTYPE html>
<html lang="en">
<head>
<meta charset="utf-8">
<title>Harnwick Aerial Services, LLC – Business Card</title>
<link href="https://fonts.googleapis.com/css2?family=Oswald:wght@300;400;600&family=Saira+Semi+Condensed:wght@700&family=Montserrat:wght@400;700&display=swap" rel="stylesheet">
<style>
  :root {
    --ink: #000000;
    --paper: #ffffff;
    --backdrop: #9b9b9b;
    --icon-fill: #e4e4e4;
  }
  * { margin: 0; padding: 0; box-sizing: border-box; }
  html, body { width: 1200px; height: 1000px; overflow: hidden; background: var(--backdrop); }
  .card {
    position: absolute; left: 211px; width: 776px; height: 447px;
    border-radius: 40px; overflow: hidden;
  }
  .card--front { top: 31px; background: var(--ink); color: var(--paper); }
  .card--back { top: 509px; background: var(--paper); color: var(--ink); }

  /* Front */
  .brand-mark {
    position: absolute; left: 336px; top: 133px; width: 104px; height: 104px;
    border: 6px solid var(--paper); border-radius: 50%;
  }
  .brand-name {
    position: absolute; left: 0; right: 0; top: 254px; text-align: center;
    font-family: "Saira Semi Condensed", sans-serif; font-weight: 700;
    font-size: 80px; line-height: 1; letter-spacing: 2px;
  }
  .brand-tagline {
    position: absolute; left: 0; right: 0; top: 339px; text-align: center;
    font-family: "Saira Semi Condensed", sans-serif; font-weight: 700;
    font-size: 30px; line-height: 1; letter-spacing: 7px; padding-left: 7px;
  }

  /* Back */
  .back-brand {
    position: absolute; left: 0; right: 0; top: 72px;
    display: flex; justify-content: center; align-items: center; gap: 14px;
  }
  .back-brand__circle { width: 46px; height: 46px; border: 4px solid var(--ink); border-radius: 50%; }
  .back-brand__name {
    font-family: "Saira Semi Condensed", sans-serif; font-weight: 700;
    font-size: 36px; letter-spacing: 2px; line-height: 1;
  }
  .person { position: absolute; right: 410px; top: 184px; text-align: right; }
  .person__name {
    font-family: "Oswald", sans-serif; font-weight: 300; font-size: 44px; line-height: 1.1;
  }
  .person__name strong { font-weight: 600; }
  .person__role {
    font-family: "Montserrat", sans-serif; font-weight: 700; font-size: 18px;
    letter-spacing: 4px; margin-top: 6px; margin-right: -4px;
  }
  .divider { position: absolute; left: 388px; top: 193px; width: 2px; height: 72px; background: var(--ink); }
  .contact { position: absolute; left: 412px; top: 192px; list-style: none; }
  .contact li {
    display: flex; align-items: center; height: 24.5px;
    font-family: "Montserrat", sans-serif; font-size: 20px; letter-spacing: 0.6px;
  }
  .contact svg { width: 16px; height: 16px; margin-right: 17px; flex: none; }

  .services { position: absolute; left: 0; top: 314px; width: 100%; }
  .service { position: absolute; top: 0; width: 150px; margin-left: -75px; text-align: center; }
  .service__icon {
    width: 57px; height: 57px; margin: 0 auto; border-radius: 50%;
    border: 1.5px solid var(--ink); background: var(--icon-fill);
  }
  .service__label {
    margin-top: 14px; font-family: "Oswald", sans-serif; font-weight: 400;
    font-size: 11px; letter-spacing: 1.8px; line-height: 15px; text-transform: uppercase;
  }
</style>
</head>
<body>
  <section class="card card--front">
    <div class="brand-mark"></div>
    <div class="brand-name">HARNWICK</div>
    <div class="brand-tagline">AERIAL SERVICES</div>
  </section>

  <section class="card card--back">
    <div class="back-brand">
      <div class="back-brand__circle"></div>
      <div class="back-brand__name">HARNWICK</div>
    </div>

    <div class="person">
      <div class="person__name">OWEN <strong>HARNWICK</strong></div>
      <div class="person__role">OWNER</div>
    </div>
    <div class="divider"></div>
    <ul class="contact">
      <li>
        <svg viewBox="0 0 24 24" aria-hidden="true"><path fill="currentColor" d="M6.6 10.8a15.1 15.1 0 0 0 6.6 6.6l2.2-2.2c.3-.3.7-.4 1-.2 1.1.4 2.3.6 3.6.6.6 0 1 .4 1 1V20c0 .6-.4 1-1 1A17 17 0 0 1 3 4c0-.6.4-1 1-1h3.5c.6 0 1 .4 1 1 0 1.3.2 2.5.6 3.6.1.3 0 .7-.2 1z"/></svg>
        (555) 014-2290
      </li>
      <li>
        <svg viewBox="0 0 24 24" aria-hidden="true"><rect x="2" y="5" width="20" height="14" fill="none" stroke="currentColor" stroke-width="2.5"/><path d="M2 5l10 8 10-8M2 19l8-7M22 19l-8-7" fill="none" stroke="currentColor" stroke-width="2"/></svg>
        harnwickaerial@mail.com
      </li>
      <li>
        <svg viewBox="0 0 24 24" aria-hidden="true"><g fill="none" stroke="currentColor" stroke-width="2"><circle cx="12" cy="12" r="10"/><ellipse cx="12" cy="12" rx="4.5" ry="10"/><path d="M2 12h20M4 7h16M4 17h16"/></g></svg>
        www.harnwickaerial.com
      </li>
    </ul>

    <div class="services">
      <div class="service" style="left:180px">
        <div class="service__icon" role="img" aria-label="Topographic contour line icon"></div>
        <div class="service__label">Thermal image<br>inspections</div>
      </div>
      <div class="service" style="left:281px">
        <div class="service__icon" role="img" aria-label="Deer head silhouette icon"></div>
        <div class="service__label">Deer<br>recovery</div>
      </div>
      <div class="service" style="left:380px">
        <div class="service__icon" role="img" aria-label="Quadcopter drone icon"></div>
        <div class="service__label">Search and<br>rescue</div>
      </div>
      <div class="service" style="left:486px">
        <div class="service__icon" role="img" aria-label="Farm tractor icon"></div>
        <div class="service__label">Custom agricultural<br>applications</div>
      </div>
      <div class="service" style="left:601px">
        <div class="service__icon" role="img" aria-label="Camera with house icon"></div>
        <div class="service__label">Real estate<br>photography</div>
      </div>
    </div>
  </section>
</body>
</html>
```